Verpackungsdesign für Pflanzentopf
Zielgruppe
Wir sind Hersteller von einem einzigartigen patentierten farbigen Pflanzensubstraten mit passendem Pflanzentopf, was zusammen ein einmaliges Pflanzensystem ergibt.
Unsere Zielgruppe sind Frauen, welche Orchideen als Zimmerpflanzen nutzen.
Aufgabenstellung
Unser Pflanzentopf soll in eine Umverpackung, welche gleichzeitig als Verkaufsverpackung dient.
Es soll eine Stanzkontur an der Verpackung enthalten sein, um den Pflanzentopf in der Verpackung sehen zu können.
Die Verpackung sollte Wertigkeit und die Genialität unseres Pflanzensystems mit seinem besonderen Nutzen vermitteln und ist gedacht für den Verkauf in Baumärkten, Gartenmärkten etc..
Unser Pflanzentopf ist 132x132 mm und 131 mm hoch
Vorteile unseres Pflanzentopfes mit unserm Orchideensubstrat zusammen im Überblick:
- versorgt die Pflanze mit Nährstoffen, kein Düngen notwendig
- hemmt Schimmel, es wächst kein Schimmel auf oder in unserem Substrat, deshalb auch für Allergiker eine Alternative
- hemmt Ungeziefer, Trauermücken, Wollläuse etc. niesten sich in unserem Boden nicht ein
- sorgt für ideale Substrat-Belüftung
- vereinfacht die Pflege von Orchideen
- vereinfacht das Gießen
- kein üblicher Schmutz wie bei anderen Pflanzenerden, bleibt sauber und zersetzt sich nicht
- das Reinigen des Topfes ist einfach, geschieht schnell und ohne den üblichen Schmutz
- ist nachhaltig, unser Substrat arbeitet als Ionenaustauscher und ist mindesten 5-8 Jahre aktiv und auch später muss nichts weggeworfen werden, weil es dann immer noch schön aussieht und trotzdem weiterverwendet werden kann

```html
<!DOCTYPE html>
<html lang="de">
<head>
<meta charset="utf-8">
<title>Varunel – Pflanzensubstrat mit Pflanzentopf</title>
<link rel="stylesheet" href="https://fonts.googleapis.com/css2?family=Montserrat:wght@800&family=Montserrat+Alternates:wght@400;600;700&display=swap">
<style>
  :root {
    --kraft: #b08a5f;
    --kraft-light: #bd9870;
    --kraft-dark: #a67d52;
    --brand-red: #d20000;
    --ink: #1f1e1b;
    --white: #ffffff;
    --orchid-tone: rgba(31, 30, 27, 0.16);
    --pot-tone: rgba(210, 0, 0, 0.55);
  }
  html, body {
    margin: 0;
    padding: 0;
    width: 1200px;
    height: 1200px;
    overflow: hidden;
  }
  .package-front {
    position: relative;
    width: 1200px;
    height: 1200px;
    background:
      radial-gradient(circle at 25% 20%, var(--kraft-light) 0%, transparent 55%),
      radial-gradient(circle at 80% 85%, var(--kraft-dark) 0%, transparent 60%),
      var(--kraft);
    font-family: "Montserrat Alternates", sans-serif;
    font-variant-ligatures: none;
    font-feature-settings: "liga" 0, "clig" 0, "dlig" 0;
    color: var(--ink);
  }
  .brand-name {
    position: absolute;
    left: 74px;
    top: 222px;
    margin: 0;
    font-family: "Montserrat Alternates", sans-serif;
    font-weight: 600;
    font-size: 136px;
    line-height: 1;
    letter-spacing: 2px;
    color: var(--brand-red);
  }
  .product-pill {
    position: absolute;
    height: 94px;
    border-radius: 47px;
    background: var(--brand-red);
    color: var(--white);
    font-family: "Montserrat", sans-serif;
    font-weight: 800;
    font-size: 41px;
    line-height: 94px;
    letter-spacing: 0.5px;
    white-space: nowrap;
    box-sizing: border-box;
  }
  .product-pill--substrate {
    left: 80px;
    top: 423px;
    width: 533px;
    padding-left: 26px;
  }
  .product-pill--pot {
    left: 127px;
    top: 505px;
    width: 532px;
    padding-left: 36px;
  }
  .target-line {
    position: absolute;
    left: 119px;
    top: 604px;
    margin: 0;
    font-weight: 700;
    font-size: 42px;
    line-height: 1.2;
    white-space: nowrap;
  }
  .target-line__highlight {
    margin-left: 6px;
  }
  .target-line__underline {
    position: absolute;
    left: 321px;
    top: 661px;
    width: 240px;
    height: 7px;
    border-radius: 4px;
    background: var(--brand-red);
  }
  .benefit-list {
    position: absolute;
    left: 119px;
    top: 716px;
    margin: 0;
    padding: 0;
    list-style: none;
    font-weight: 700;
    font-size: 24.5px;
    line-height: 37.3px;
    white-space: nowrap;
  }
  .benefit-list li::before {
    content: "- ";
  }
  .orchid-area {
    position: absolute;
    left: 733px;
    top: 112px;
    width: 408px;
    height: 600px;
    border-radius: 200px 200px 60px 60px;
    background: radial-gradient(ellipse at 50% 40%, var(--orchid-tone) 0%, rgba(31, 30, 27, 0.06) 75%, transparent 100%);
  }
  .pot-area {
    position: absolute;
    left: 742px;
    top: 722px;
    width: 353px;
    height: 332px;
    border-radius: 10px 10px 14px 14px;
    background: var(--pot-tone);
  }
  .saucer-area {
    position: absolute;
    left: 696px;
    top: 1063px;
    width: 438px;
    height: 72px;
    border-radius: 36px;
    background: var(--pot-tone);
  }
  .sustainable-badge {
    position: absolute;
    left: 124px;
    top: 984px;
    width: 96px;
    height: 96px;
  }
  .sustainable-label {
    position: absolute;
    left: 74px;
    top: 1093px;
    width: 200px;
    text-align: center;
    font-weight: 400;
    font-size: 21px;
    line-height: 1.2;
  }
</style>
</head>
<body>
  <main class="package-front">
    <h1 class="brand-name">varunel</h1>

    <div class="product-pill product-pill--substrate">PFLANZENSUBSTRAT</div>
    <div class="product-pill product-pill--pot">MIT PFLANZENTOPF</div>

    <p class="target-line">für deine <span class="target-line__highlight">Orchideen</span></p>
    <div class="target-line__underline"></div>

    <ul class="benefit-list">
      <li>versorgt die Pflanze mit Nährstoffen</li>
      <li>hemmt Schimmel und Ungeziefer</li>
      <li>sorgt für ideale Substrat-Belüftung</li>
      <li>vereinfacht die Pflege von Orchideen</li>
      <li>vereinfacht das Gießen</li>
    </ul>

    <div class="orchid-area" role="img" aria-label="Strichzeichnung: Orchidee mit zwei Blüten, Knospen und Blättern"></div>
    <div class="pot-area" role="img" aria-label="Strichzeichnung: roter Pflanzentopf mit Punktmuster"></div>
    <div class="saucer-area" role="img" aria-label="Strichzeichnung: roter Untersetzer"></div>

    <svg class="sustainable-badge" viewBox="0 0 96 96" aria-hidden="true">
      <circle cx="48" cy="48" r="45" fill="none" stroke="var(--ink)" stroke-width="3"/>
    </svg>
    <div class="sustainable-label">nachhaltig</div>
  </main>
</body>
</html>
```